Vela Norvina is a dietary supplement company and in need of label design for 4 products

label for 4 dietary supplement products :1- Biotin. Red bottle ( please see the picture attached, not the whole bottle is colored but rather its a white bottle with the upper part and lower part of the bottle colored)2- COQ10. Orange Bottle 3- Hair Skin Nail. Pink bottle 4- Probiotics. Green Bottle we like the label to:1- have a modern and sleek appearance with very limited graphics.2- have a transparent background( as the bottle is white )3- have the box with the supplement and ingredient to appear sideways( horizontal )4- to have a color matching the bottle color.attached you will find :1- the dimension of the bottle.2- four different labels for each of the products.3- two pictures of the bottles 4- picture of the caps5- Logo
Industry/Entity Type
Health And Wellness
Colors
Designer to choose colors to be used in the design.
Look and feel
Each slider illustrates characteristics of the customer's brand and the style your logo design should communicate.

```html
<!DOCTYPE html>
<html lang="en">
<head>
<meta charset="utf-8">
<title>Vela Norvina – Supplement Labels</title>
<link rel="stylesheet" href="https://fonts.googleapis.com/css2?family=Oswald:wght@300;400;500&family=Saira:wght@300;400&family=Saira+Semi+Condensed:wght@400;500&display=swap">
<style>
  :root {
    --bg: #ececec;
    --label: #ffffff;
    --ink: #3c3c3c;
    --ink-soft: #5b5b5b;
    --pill: #5e5e5e;
    --leaf: #3f8a2c;
    --supplement: #4e7d2a;
    --seal: #d9a21c;
    --biotin: #e8141c;
    --coq10: #e5611a;
    --coq10-band: #f77a06;
    --hsn: #e0127a;
    --hsn-band: #ff1493;
  }
  * { box-sizing: border-box; margin: 0; padding: 0; }
  html, body { width: 1200px; height: 1133px; overflow: hidden; }
  body {
    background: var(--bg);
    font-family: "Oswald", sans-serif;
    color: var(--ink);
  }
  .label-row {
    position: absolute;
    top: 330px;
    left: 0;
    width: 1200px;
    display: flex;
    justify-content: center;
    gap: 70px;
  }
  .label {
    position: relative;
    width: 300px;
    height: 520px;
    background: var(--label);
    border-radius: 6px;
    box-shadow: 0 8px 24px rgba(0,0,0,0.10);
    overflow: hidden;
    text-align: center;
  }
  .label__band { height: 34px; background: var(--accent-band); }
  .brand {
    margin: 38px auto 0;
    display: flex;
    align-items: center;
    justify-content: center;
    gap: 8px;
    font-family: "Oswald", sans-serif;
    font-weight: 400;
    font-size: 26px;
    color: var(--ink);
    letter-spacing: 0.5px;
  }
  .brand__mark { width: 12px; height: 12px; background: var(--leaf); }
  .product-name {
    margin-top: 22px;
    font-family: "Saira", sans-serif;
    font-weight: 300;
    font-size: 72px;
    line-height: 0.95;
    color: var(--accent);
    letter-spacing: 1px;
  }
  .product-name--stacked { font-size: 50px; line-height: 1; margin-top: 12px; }
  .pill {
    display: inline-block;
    margin-top: 10px;
    padding: 3px 10px;
    background: var(--pill);
    color: #fff;
    border-radius: 14px;
    font-family: "Oswald", sans-serif;
    font-weight: 500;
    font-size: 10.5px;
    white-space: nowrap;
  }
  .pill--wide { font-size: 14px; letter-spacing: 4px; padding: 3px 16px; }
  .facts {
    display: flex;
    align-items: stretch;
    margin: 26px 0 0 40px;
    text-align: left;
  }
  .count {
    padding-right: 14px;
    border-right: 1px solid #bdbdbd;
    font-family: "Saira Semi Condensed", sans-serif;
    color: var(--ink-soft);
  }
  .count__num { display: block; font-size: 52px; line-height: 0.9; font-weight: 400; }
  .count__unit { display: block; font-family: "Oswald", sans-serif; font-size: 13px; font-weight: 500; }
  .benefits { list-style: none; padding-left: 12px; }
  .benefits li {
    position: relative;
    padding-left: 14px;
    font-size: 11.5px;
    font-weight: 300;
    line-height: 21px;
    color: var(--ink-soft);
    white-space: nowrap;
  }
  .benefits li::before {
    content: "";
    position: absolute;
    left: 0; top: 6px;
    width: 8px; height: 8px;
    background: var(--leaf);
    border-radius: 0 8px 0 8px;
  }
  .seal {
    position: absolute;
    right: 22px;
    bottom: 58px;
    width: 44px; height: 44px;
    border-radius: 50%;
    background: var(--seal);
  }
  .dietary {
    position: absolute;
    left: 0; right: 0;
    bottom: 26px;
    font-family: "Oswald", sans-serif;
    font-weight: 400;
    font-size: 13px;
    letter-spacing: 3px;
    color: var(--supplement);
  }
  .label--biotin { --accent: var(--biotin); --accent-band: var(--biotin); }
  .label--coq10 { --accent: var(--coq10); --accent-band: var(--coq10-band); }
  .label--hsn { --accent: var(--hsn); --accent-band: var(--hsn-band); }
</style>
</head>
<body>
  <main class="label-row">
    <section class="label label--biotin">
      <div class="label__band"></div>
      <div class="brand"><span class="brand__mark"></span>Vela Norvina</div>
      <h1 class="product-name">BIOTIN</h1>
      <span class="pill">100% PURE BIOTIN FOR FOR HAIR, SKIN AND NAILS</span>
      <div class="facts">
        <div class="count"><span class="count__num">60</span><span class="count__unit">CAPSULES</span></div>
        <ul class="benefits">
          <li>Healthy Hair, Skin and Nails</li>
          <li>Reduce excessive dryness</li>
          <li>Cures Fragile nails</li>
          <li>Reduce Hairfall</li>
        </ul>
      </div>
      <div class="seal" role="img" aria-label="Quality seal"></div>
      <p class="dietary">DIETARY SUPPLEMENT</p>
    </section>

    <section class="label label--coq10">
      <div class="label__band"></div>
      <div class="brand"><span class="brand__mark"></span>Vela Norvina</div>
      <h1 class="product-name">COQ10</h1>
      <span class="pill">(UBIQUINONE) HIGH ABSORPTION VEGAN COENZYME</span>
      <div class="facts">
        <div class="count"><span class="count__num">60</span><span class="count__unit">CAPSULES</span></div>
        <ul class="benefits">
          <li>With superior absorption</li>
          <li>100% water and fat-soluble</li>
          <li>Supports heart and vascular health</li>
          <li>Powerful Antioxidant</li>
        </ul>
      </div>
      <div class="seal" role="img" aria-label="Quality seal"></div>
      <p class="dietary">DIETARY SUPPLEMENT</p>
    </section>

    <section class="label label--hsn">
      <div class="label__band"></div>
      <div class="brand"><span class="brand__mark"></span>Vela Norvina</div>
      <h1 class="product-name product-name--stacked">HAIR, SKIN<br>&amp; NAILS</h1>
      <span class="pill pill--wide">ESSENTIALS</span>
      <div class="facts">
        <div class="count"><span class="count__num">60</span><span class="count__unit">CAPSULES</span></div>
        <ul class="benefits">
          <li>Rich in Biotin</li>
          <li>Vital Nutrients</li>
          <li>Care for Hair, Skin &amp; Nails</li>
          <li>Glowing Skin</li>
        </ul>
      </div>
      <div class="seal" role="img" aria-label="Quality seal"></div>
      <p class="dietary">DIETARY SUPPLEMENT</p>
    </section>
  </main>
</body>
</html>
```